Your Joint Helper - Orthopedic needs from one site

We need slides that help to educate users, interest investors and allow the complexity of the entire continuum of care to be explained so anyone can understand. Your Joint Helper is a Varomin Health Company. Yourjointhelperhub.example. We allow people to evaluate, educate and engage with providers from one site. Simplyfying orthopedic care and wellness from one site. Patients, doctors, personal trainers, therapist, nutritionist, yoga, gyms, athletic trainers and more can connect from one site

Target Market(s)

Investors, Patients, Doctors and wellness providers

Industry/Entity Type

Healthcare

Requirements
Must have
• Investor slides, sales slides, education, process....

```html
<!DOCTYPE html>
<html lang="en">
<head>
<meta charset="utf-8">
<title>Your Joint Helper — Slide Deck Overview</title>
<link href="https://fonts.googleapis.com/css2?family=Montserrat:wght@400;500;600;700;800&display=swap" rel="stylesheet">
<style>
  :root{
    --navy:#0c2165;
    --navy-deep:#081a52;
    --green:#5bb246;
    --green-light:#8cc63f;
    --teal:#2e9a8a;
    --blue:#2f72bf;
    --ink:#3a3a3a;
    --muted:#8a8a8a;
    --photo-skin:#c9d3dc;
    --photo-shirt:#7fa6b5;
    --paper:#ffffff;
  }
  *{box-sizing:border-box;margin:0;padding:0}
  html,body{width:1200px;height:1200px;overflow:hidden;background:var(--paper);font-family:"Montserrat",sans-serif}
  .canvas{position:relative;width:1200px;height:1200px}
  .slide{position:absolute;width:338px;height:190px;overflow:hidden;background:var(--paper);box-shadow:0 2px 7px rgba(0,0,0,.22)}
  .slide > *{position:absolute}
  .navy{background:var(--navy)}
  .brand{display:flex;align-items:center;gap:2px;font-size:3.6px;font-weight:700;color:var(--green);letter-spacing:.1px;text-transform:uppercase;line-height:1}
  .brand::before{content:"";width:6px;height:6px;border-radius:50%;background:var(--blue)}
  .brand.on-dark{color:var(--green-light)}
  .brand.on-dark::before{background:var(--green-light)}
  .title{font-weight:700;color:var(--green);line-height:1.05;letter-spacing:-.1px}
  .title.grad{background:linear-gradient(90deg,var(--green),var(--teal));-webkit-background-clip:text;background-clip:text;color:transparent}
  .body{font-size:4.2px;line-height:1.75;color:var(--ink)}
  .body.light{color:#dfe6f5}
  .small{font-size:3.4px;line-height:1.6;color:var(--muted)}
  .label{font-size:4.6px;font-weight:600;color:var(--ink)}
  .btn{background:var(--blue);color:#fff;font-size:3.6px;font-weight:700;border-radius:4px;padding:1.4px 9px;line-height:1.4}
  .foot-left,.foot-right{bottom:4px;font-size:2.8px;color:var(--muted)}
  .foot-left{left:26px}
  .foot-left b{color:var(--green)}
  .foot-right{right:26px}
  .on-dark-foot{color:#fff}
  .photo{background:linear-gradient(160deg,#dde4ea,var(--photo-shirt) 70%,#5e8797)}
  .photo.desk{background:linear-gradient(150deg,#e6e1d7,#c9b79a 60%,#7f9a6b)}
  .photo.xray{background:radial-gradient(ellipse at 45% 50%,#6f8fa8,#1c3347 60%,#07131e)}
  .photo.clinic{background:linear-gradient(150deg,#33466a,#25385e 60%,#1a2b4d)}
  .photo.tablet{background:linear-gradient(150deg,#eef2f5,#b7c4cf 55%,#6c7c8a)}
  .card{background:#fff;box-shadow:0 1px 3px rgba(0,0,0,.18)}
  .icon-dot{border-radius:50%}
</style>
</head>
<body>
<div class="canvas">

  <!-- 1 Cover -->
  <section class="slide" style="left:69px;top:166px">
    <div class="photo clinic" role="img" aria-label="Physiotherapist treating a patient in a clinic, blue tint" style="inset:0"></div>
    <div style="inset:0;background:rgba(12,33,101,.72)"></div>
    <div class="title" style="left:39px;top:62px;font-size:11.5px;font-weight:800">YOUR TITLE<br>PRESENTATION<br>GOES HERE</div>
    <div style="left:39px;top:107px;font-size:6px;line-height:1.15;color:var(--green)">YOU COULD PLACE YOUR<br>SUBTITLE PRESENTATION<br>HERE</div>
    <svg style="left:171px;top:26px" width="145" height="145" viewBox="0 0 145 145"><circle cx="72.5" cy="72.5" r="70" fill="none" stroke="var(--green)" stroke-width="3"/></svg>
    <div style="left:214px;top:78px;font-size:10px;font-weight:600;color:#fff;line-height:1.25">YOUR JOINT<br>HELPER</div>
  </section>

  <!-- 2 About Us -->
  <section class="slide" style="left:441px;top:166px">
    <div class="brand" style="left:22px;top:12px">Your Joint Helper</div>
    <div class="photo" role="img" aria-label="Man in a blue t-shirt holding his lower back" style="left:0;top:36px;width:160px;height:154px;border-radius:0 80px 0 0"></div>
    <svg style="left:0;top:32px" width="180" height="158" viewBox="0 0 180 158"><path d="M0 14 Q95 -22 150 60 Q178 110 160 158" fill="none" stroke="var(--green)" stroke-width="3"/><path d="M0 14 Q60 -6 105 18" fill="none" stroke="var(--blue)" stroke-width="3"/></svg>
    <div class="title grad" style="right:27px;top:24px;font-size:15px">About Us</div>
    <p class="body" style="right:27px;top:47px;width:128px;text-align:right;line-height:2.1">Lorem ipsum is simply dummy text of the printing and typesetting industry. Lorem ipsum has been the industry's standard dummy text ever since the 1500s, when an unknown printer took a galley of type and scrambled it to make a type specimen book. It has survived not only five centuries, but also the leap into electronic typesetting, remaining essentially unchanged. It was popularized in the 1960s with the release of Typesheet sheets containing lorem ipsum passages, and more recently with desktop publishing software like Pageform Studio.</p>
    <div class="btn" style="right:26px;top:160px">learn now</div>
    <div class="foot-right" style="right:25px">www.yourjointhelperhub.example &nbsp;| 2</div>
  </section>

  <!-- 3 Evaluate Now -->
  <section class="slide" style="left:801px;top:166px">
    <div style="left:0;top:102px;width:338px;height:88px;background:linear-gradient(180deg,var(--navy) 20%,var(--teal) 80%,var(--green))"></div>
    <div class="brand" style="left:22px;top:12px">Your Joint Helper</div>
    <div class="title grad" style="left:24px;top:36px;font-size:15px">Evaluate<br>Now</div>
    <p class="body" style="left:130px;top:38px;width:186px;font-size:3.6px;text-align:justify;color:var(--muted)">Lorem ipsum is simply dummy text of the printing and typesetting industry. Lorem ipsum has been the industry's standard dummy text ever since the 1500s, when an unknown printer took a galley of type and scrambled it to make a type specimen book. It has survived not only five centuries, but also the leap into electronic typesetting, remaining essentially unchanged. It was popularized in the 1960s with the release of</p>
    <div style="left:35px;top:87px;display:grid;grid-template-columns:repeat(3,86px);gap:4px 4px">
      <div class="card" style="height:33px;padding:6px 0 0 26px"><span class="label" style="font-size:4px">description</span><p class="small">suscipit eros iste metus<br>auctor id dapibus quam</p></div>
      <div class="card" style="height:33px;padding:6px 0 0 26px"><span class="label" style="font-size:4px">description</span><p class="small">suscipit eros iste metus<br>auctor id dapibus quam</p></div>
      <div class="card" style="height:33px;padding:6px 0 0 26px"><span class="label" style="font-size:4px">description</span><p class="small">suscipit eros iste metus<br>auctor id dapibus quam</p></div>
      <div class="card" style="height:33px;padding:6px 0 0 26px"><span class="label" style="font-size:4px">description</span><p class="small">suscipit eros iste metus<br>auctor id dapibus quam</p></div>
      <div class="card" style="height:33px;padding:6px 0 0 26px"><span class="label" style="font-size:4px">description</span><p class="small">suscipit eros iste metus<br>auctor id dapibus quam</p></div>
      <div class="card" style="height:33px;padding:6px 0 0 26px"><span class="label" style="font-size:4px">description</span><p class="small">suscipit eros iste metus<br>auctor id dapibus quam</p></div>
    </div>
    <div class="icon-dot" style="left:44px;top:96px;width:10px;height:10px;background:var(--green)"></div>
    <div class="icon-dot" style="left:134px;top:96px;width:10px;height:10px;background:var(--green)"></div>
    <div class="icon-dot" style="left:224px;top:96px;width:10px;height:10px;background:var(--green)"></div>
    <div class="icon-dot" style="left:44px;top:133px;width:10px;height:10px;background:var(--green)"></div>
    <div class="icon-dot" style="left:134px;top:133px;width:10px;height:10px;background:var(--green)"></div>
    <div class="icon-dot" style="left:224px;top:133px;width:10px;height:10px;background:var(--green)"></div>
    <div class="foot-left on-dark-foot" style="font-weight:600">Simplifying <b style="color:#fff">YOUR</b> Orthopedic Care</div>
    <div class="foot-right on-dark-foot" style="font-weight:600">www.yourjointhelperhub.example &nbsp;| 3</div>
  </section>

  <!-- 4 Ask about your topic -->
  <section class="slide" style="left:69px;top:394px">
    <div class="brand" style="left:22px;top:12px">Your Joint Helper</div>
    <div class="photo desk" role="img" aria-label="Doctor reviewing a hand x-ray on a tablet at a desk with a plant" style="left:225px;top:0;width:113px;height:190px"></div>
    <div class="title grad" style="left:23px;top:34px;font-size:15px">Ask about your topic</div>
    <p class="body" style="left:23px;top:55px;width:185px">Lorem ipsum is simply dummy text of the printing and typesetting industry. Lorem ipsum has been the industry's standard dummy text ever since the 1500s, when an unknown printer took a galley of type and</p>
    <div class="btn" style="left:23px;top:86px">learn now</div>
    <div class="label" style="left:23px;top:101px;font-size:4.6px">● description</div>
    <p class="small" style="left:23px;top:109px;width:130px;color:var(--ink)">Lorem ipsum is simply dummy text of the printing and typesetting industry. Lorem ipsum has been the industry's standard dummy text ever since the 1500s, when</p>
    <div class="label" style="left:23px;top:137px;font-size:4.6px">● description</div>
    <p class="small" style="left:23px;top:145px;width:130px;color:var(--ink)">Lorem ipsum is simply dummy text of the printing and typesetting industry. Lorem ipsum has been the industry's standard dummy text ever since the 1500s, when</p>
    <div style="left:194px;top:101px;width:58px;height:72px;background:var(--blue);border-radius:3px;color:#fff;text-align:center;padding-top:32px">
      <div style="font-size:4.6px;font-weight:700">description</div>
      <div style="font-size:3.5px;line-height:1.7;margin-top:3px">nullam eu tempor<br>purus nunc a leo<br>magna sit</div>
    </div>
    <div class="foot-left">Simplifying <b>YOUR</b> Orthopedic Care</div>
    <div class="foot-right">www.yourjointhelperhub.example &nbsp;| 4</div>
  </section>

  <!-- 5 Ask about your topic, navy header -->
  <section class="slide" style="left:441px;top:394px">
    <div class="navy" style="left:0;top:0;width:225px;height:115px"></div>
    <div class="photo tablet" role="img" aria-label="Hands holding a tablet showing a knee scan" style="left:225px;top:0;width:113px;height:115px"></div>
    <div class="brand on-dark" style="left:22px;top:12px">Your Joint Helper</div>
    <div class="title grad" style="left:23px;top:33px;font-size:15px">Ask about your topic</div>
    <p class="body light" style="left:24px;top:54px;width:175px">Lorem ipsum is simply dummy text of the printing and typesetting industry. Lorem ipsum has been the industry's standard dummy text ever since the 1500s, when an unknown printer took a galley of type and scrambled it to make a type specimen book. It has survived not</p>
    <div class="btn" style="left:24px;top:95px">learn now</div>
    <div class="icon-dot" style="left:23px;top:128px;width:40px;height:40px;background:var(--navy);border:2px solid #fff;box-shadow:0 0 0 1px var(--blue)"></div>
    <div class="label" style="left:70px;top:130px">description</div>
    <p class="small" style="left:70px;top:139px;width:84px">the leap into electronic typesetting, remaining essentially unchanged. It was popularized in the 1960s with the release of sheets containing lorem</p>
    <div class="icon-dot" style="left:174px;top:128px;width:40px;height:40px;background:var(--navy);border:2px solid #fff;box-shadow:0 0 0 1px var(--blue)"></div>
    <div class="label" style="left:221px;top:130px">description</div>
    <p class="small" style="left:221px;top:139px;width:84px">lorem passages, and more recently with desktop publishing software including versions of lorem ipsum debitis non cum nobis nam id</p>
  </section>

  <!-- 6 Ask about your topic, header band + cards -->
  <section class="slide" style="left:801px;top:394px">
    <div class="navy" style="left:0;top:0;width:338px;height:71px"></div>
    <div class="brand on-dark" style="left:22px;top:12px">Your Joint Helper</div>
    <div class="title grad" style="left:0;width:338px;text-align:center;top:21px;font-size:15px">Ask about your topic</div>
    <p class="body light" style="left:34px;width:270px;top:42px;text-align:center;font-size:3.6px">Lorem ipsum is simply dummy text of the printing and typesetting industry. Lorem ipsum has been the industry's standard dummy text ever since the 1500s, when an unknown printer took a galley of type and scrambled it to make a type</p>
    <div class="btn" style="left:149px;top:67px">learn now</div>
    <div style="left:35px;top:84px;display:grid;grid-template-columns:repeat(2,85px);gap:4px 3px">
      <div class="card" style="height:41px;padding:5px 4px 0 26px"><div class="label" style="font-size:4.2px;text-align:center">company profile</div><p class="small" style="text-align:justify">the leap into electronic typesetting, remaining essentially unchanged. It</p></div>
      <div class="card" style="height:41px;padding:5px 4px 0 26px"><div class="label" style="font-size:4.2px;text-align:center">meet our teams</div><p class="small" style="text-align:justify">the leap into electronic typesetting, remaining essentially unchanged. It</p></div>
      <div class="card" style="height:41px;padding:5px 4px 0 26px"><div class="label" style="font-size:4.2px;text-align:center">image gallery</div><p class="small" style="text-align:justify">the leap into electronic typesetting, remaining essentially unchanged. It</p></div>
      <div class="card" style="height:41px;padding:5px 4px 0 26px"><div class="label" style="font-size:4.2px;text-align:center">infographics</div><p class="small" style="text-align:justify">the leap into electronic typesetting, remaining essentially unchanged. It</p></div>
    </div>
    <svg style="left:42px;top:97px" width="12" height="12" viewBox="0 0 12 12"><path d="M1 6 L5 10 L11 1" fill="none" stroke="var(--green)" stroke-width="2"/></svg>
    <div class="icon-dot" style="left:130px;top:98px;width:10px;height:10px;background:var(--green)"></div>
    <div class="icon-dot" style="left:42px;top:143px;width:10px;height:10px;background:var(--green)"></div>
    <div class="icon-dot" style="left:130px;top:143px;width:10px;height:10px;background:var(--green)"></div>
    <div class="photo xray" role="img" aria-label="Doctor holding a spine x-ray film" style="left:216px;top:85px;width:86px;height:86px"></div>
    <div class="foot-left">Simplifying <b>YOUR</b> Orthopedic Care</div>
    <div class="foot-right">www.yourjointhelperhub.example &nbsp;| 6</div>
  </section>

  <!-- 7 Four circles -->
  <section class="slide" style="left:69px;top:623px">
    <div class="brand" style="left:22px;top:12px">Your Joint Helper</div>
    <div class="title grad" style="left:0;width:338px;text-align:center;top:20px;font-size:15px">Ask about your topic</div>
    <p class="body" style="left:36px;width:266px;top:41px;text-align:center;font-size:3.6px;color:var(--muted)">Lorem ipsum is simply dummy text of the printing and typesetting industry. Lorem ipsum has been the industry's standard dummy text ever since the 1500s, when an unknown printer took a galley of type and scrambled it to make a type</p>
    <div class="btn" style="left:148px;top:60px">learn now</div>
    <div class="icon-dot" style="left:53px;top:80px;width:36px;height:36px;background:var(--green-light);border:2px solid #fff;box-shadow:0 0 0 1px var(--green-light)"></div>
    <div class="icon-dot" style="left:120px;top:80px;width:36px;height:36px;background:var(--green);border:2px solid #fff;box-shadow:0 0 0 1px var(--green)"></div>
    <div class="icon-dot" style="left:187px;top:80px;width:36px;height:36px;background:#3fa55a;border:2px solid #fff;box-shadow:0 0 0 1px #3fa55a"></div>
    <div class="icon-dot" style="left:254px;top:80px;width:36px;height:36px;background:var(--blue);border:2px solid #fff;box-shadow:0 0 0 1px var(--blue)"></div>
    <div style="left:43px;top:124px;width:256px;display:grid;grid-template-columns:repeat(4,56px);gap:11px;text-align:center">
      <div><div class="label" style="font-size:4.4px">description</div><p class="small" style="text-align:justify;color:var(--ink)">the leap into electronic typesetting, remaining essentially unchanged. It was popularized in the 1960s with the release of</p></div>
      <div><div class="label" style="font-size:4.4px">description</div><p class="small" style="text-align:justify;color:var(--ink)">the leap into electronic typesetting, remaining essentially unchanged. It was popularized in the 1960s with the release of</p></div>
      <div><div class="label" style="font-size:4.4px">description</div><p class="small" style="text-align:justify;color:var(--ink)">the leap into electronic typesetting, remaining essentially unchanged. It was popularized in the 1960s with the release of</p></div>
      <div><div class="label" style="font-size:4.4px">description</div><p class="small" style="text-align:justify;color:var(--ink)">the leap into electronic typesetting, remaining essentially unchanged. It was popularized in the 1960s with the release of</p></div>
    </div>
    <div class="foot-left">Simplifying <b>YOUR</b> Orthopedic Care</div>
    <div class="foot-right">www.yourjointhelperhub.example &nbsp;| 7</div>
  </section>

  <!-- 8 Three highlighted points over photo -->
  <section class="slide" style="left:441px;top:623px">
    <div class="brand" style="left:22px;top:12px">Your Joint Helper</div>
    <div class="photo" role="img" aria-label="Man in a blue t-shirt seen from behind, hand on his shoulder" style="left:187px;top:0;width:151px;height:190px"></div>
    <div class="title grad" style="left:25px;top:36px;font-size:15px">Ask about<br>your topic</div>
    <p class="body" style="left:25px;top:77px;width:125px">Lorem ipsum is simply dummy text of the printing and typesetting industry. Lorem ipsum has been the industry's standard dummy text ever since the 1500s, when an unknown printer took a galley of type and scrambled it to make a type specimen book. It has survived not only five centuries, but also</p>
    <div class="btn" style="left:25px;top:152px">learn now</div>
    <div style="left:170px;top:26px;width:158px;height:20px;background:rgba(91,178,70,.85)"></div>
    <div style="left:170px;top:76px;width:158px;height:20px;background:rgba(91,178,70,.85)"></div>
    <div style="left:170px;top:126px;width:158px;height:20px;background:rgba(46,154,138,.85)"></div>
    <div class="icon-dot" style="left:168px;top:24px;width:37px;height:37px;background:var(--green);border:2px solid #fff"></div>
    <div class="icon-dot" style="left:168px;top:74px;width:37px;height:37px;background:var(--green);border:2px solid #fff"></div>
    <div class="icon-dot" style="left:168px;top:124px;width:37px;height:37px;background:var(--blue);border:2px solid #fff"></div>
    <div style="left:215px;top:31px;color:#fff;font-size:3.6px;line-height:1.6"><b style="font-size:4.4px">description</b><br>suscipit eros iste metus auctor id dapibus quam<br>aliquam sed pretium viverra ornare praesent</div>
    <div style="left:215px;top:81px;color:#fff;font-size:3.6px;line-height:1.6"><b style="font-size:4.4px">description</b><br>suscipit eros iste metus auctor id dapibus quam<br>aliquam sed pretium viverra ornare praesent</div>
    <div style="left:215px;top:131px;color:#fff;font-size:3.6px;line-height:1.6"><b style="font-size:4.4px">description</b><br>suscipit eros iste metus auctor id dapibus quam<br>aliquam sed pretium viverra ornare praesent</div>
    <div class="foot-left">Simplifying <b>YOUR</b> Orthopedic Care</div>
    <div class="foot-right on-dark-foot" style="font-weight:600">www.yourjointhelperhub.example</div>
  </section>

  <!-- 9 Photo grid -->
  <section class="slide" style="left:801px;top:623px">
    <div class="brand" style="left:22px;top:12px">Your Joint Helper</div>
    <div class="title grad" style="left:23px;top:40px;font-size:15px">Ask about your topic</div>
    <p class="body" style="left:23px;top:60px;width:175px;text-align:justify">Lorem ipsum is simply dummy text of the printing and typesetting industry. Lorem ipsum has been the industry's standard dummy text ever since the 1500s, when an unknown printer took a galley of type and scrambled it to make a type specimen book. It has survived not only five centuries, but also the leap into electronic typesetting.</p>
    <p class="small" style="left:23px;top:114px;width:127px;text-align:justify;color:var(--ink)">Lorem ipsum is simply dummy text of the printing and typesetting industry. Lorem ipsum has been the industry's standard dummy text ever since the 1500s, when an unknown printer took a galley of type and scrambled it to make a type specimen book. It has survived not only five centuries, but also the leap into electronic typesetting.</p>
    <div class="btn" style="left:23px;top:167px">learn now</div>
    <div class="photo desk" role="img" aria-label="Tablet showing a hand scan" style="left:218px;top:17px;width:49px;height:49px"></div>
    <div class="photo" role="img" aria-label="Man holding his back" style="left:272px;top:17px;width:49px;height:49px"></div>
    <div class="photo xray" role="img" aria-label="Spine x-ray film" style="left:218px;top:70px;width:49px;height:49px"></div>
    <div class="photo clinic" role="img" aria-label="Clinic treatment room" style="left:272px;top:70px;width:49px;height:49px"></div>
    <div class="photo tablet" role="img" aria-label="Tablet with a knee scan" style="left:164px;top:123px;width:49px;height:49px"></div>
    <div class="photo desk" role="img" aria-label="Doctor at a desk with a tablet" style="left:218px;top:123px;width:49px;height:49px"></div>
    <div class="photo" role="img" aria-label="Digital body scan in blue" style="left:272px;top:123px;width:49px;height:49px;background:linear-gradient(150deg,#4d7ab0,#2a4f86 60%,#1b3564)"></div>
    <div class="foot-left">Simplifying <b>YOUR</b> Orthopedic Care</div>
    <div class="foot-right">www.yourjointhelperhub.example &nbsp;| 9</div>
  </section>

  <!-- 10 Three photos -->
  <section class="slide" style="left:69px;top:851px">
    <div class="brand" style="left:22px;top:12px">Your Joint Helper</div>
    <div class="title grad" style="left:0;width:338px;text-align:center;top:28px;font-size:15px">Ask about your topic</div>
    <div class="photo" role="img" aria-label="Man holding his lower back" style="left:34px;top:61px;width:68px;height:68px"></div>
    <div class="photo tablet" role="img" aria-label="Hands holding a tablet with a knee scan" style="left:135px;top:61px;width:68px;height:68px"></div>
    <div class="photo desk" role="img" aria-label="Tablet showing a hand scan on a desk" style="left:235px;top:61px;width:68px;height:68px"></div>
    <div class="icon-dot" style="left:60px;top:122px;width:16px;height:16px;background:var(--green);border:1.5px solid #fff"></div>
    <div class="icon-dot" style="left:161px;top:122px;width:16px;height:16px;background:var(--green);border:1.5px solid #fff"></div>
    <div class="icon-dot" style="left:261px;top:122px;width:16px;height:16px;background:var(--blue);border:1.5px solid #fff"></div>
    <div style="left:30px;top:142px;width:286px;display:grid;grid-template-columns:repeat(3,80px);gap:20px;text-align:center">
      <div><div class="label" style="font-size:4.4px">description</div><p class="small" style="font-style:italic">Lorem ipsum is simply dummy text of the printing and typesetting industry</p></div>
      <div><div class="label" style="font-size:4.4px">description</div><p class="small" style="font-style:italic">Lorem ipsum is simply dummy text of the printing and typesetting industry</p></div>
      <div><div class="label" style="font-size:4.4px">description</div><p class="small" style="font-style:italic">Lorem ipsum is simply dummy text of the printing and typesetting industry</p></div>
    </div>
    <div class="foot-left">Simplifying <b>YOUR</b> Orthopedic Care</div>
    <div class="foot-right">www.yourjointhelperhub.example &nbsp;| 10</div>
  </section>

  <!-- 11 Navy feature -->
  <section class="slide navy" style="left:441px;top:851px">
    <div style="left:0;top:12px;width:125px;height:166px;background:#fff"></div>
    <div class="photo" role="img" aria-label="Man in a blue t-shirt holding his lower back" style="left:0;top:12px;width:125px;height:166px"></div>
    <div class="photo xray" role="img" aria-label="Spine x-ray film held up" style="left:130px;top:108px;width:70px;height:82px"></div>
    <div class="brand on-dark" style="right:16px;top:12px">Your Joint Helper</div>
    <div class="title grad" style="right:25px;top:38px;font-size:15px">Ask about your topic</div>
    <p class="body light" style="right:25px;top:61px;width:165px;text-align:right;color:#fff;font-size:3.8px">Lorem ipsum is simply dummy text of the printing and typesetting industry. Lorem ipsum has been the industry's standard dummy text ever since the 1500s, when an unknown printer took a galley of type and scrambled it to make a type specimen book. It has survived not only five centuries, but also the leap into electronic typesetting.</p>
    <div class="btn" style="right:23px;top:159px">learn now</div>
    <div class="foot-left on-dark-foot" style="font-weight:600">Simplifying <b>YOUR</b> Orthopedic Care</div>
    <div class="foot-right on-dark-foot" style="font-weight:600">www.yourjointhelperhub.example &nbsp;| 11</div>
  </section>

  <!-- 12 Two photos -->
  <section class="slide" style="left:801px;top:851px">
    <div class="brand" style="left:22px;top:12px">Your Joint Helper</div>
    <div class="title grad" style="left:26px;top:36px;font-size:15px">Ask about<br>your topic</div>
    <p class="body" style="left:23px;top:76px;width:143px;text-align:justify">Lorem ipsum is simply dummy text of the printing and typesetting industry. Lorem ipsum has been the industry's standard dummy text ever since the 1500s, when an unknown printer took a galley of type and scrambled it to make a type specimen book. It has survived not only five centuries, but also the leap into electronic typesetting. Lorem ipsum is simply dummy text of the printing and typesetting industry. Lorem</p>
    <div class="btn" style="left:23px;top:158px">learn now</div>
    <div class="photo" role="img" aria-label="Doctor examining a man's back" style="left:190px;top:28px;width:113px;height:65px"></div>
    <div class="photo xray" role="img" aria-label="Doctor holding a spine x-ray film" style="left:190px;top:98px;width:125px;height:65px"></div>
    <div class="foot-left">Simplifying <b>YOUR</b> Orthopedic Care</div>
    <div class="foot-right">www.yourjointhelperhub.example &nbsp;| 12</div>
  </section>

</div>
</body>
</html>
```